App für weniger Konsum
Zielgruppe
Wir sind ein Startup, das Nutzer:innen in einem bewussteren Kaufverhalten stärkt. Dabei werden Nutzer:innen psychologischen Kaufprofilen zugeordnet und individuell auf dem Weg begleitet, weniger einzukaufen. Das stärkt die Finanzen und schützt die Umwelt.
Aufgabenstellung
Das Design sollte einerseits minimalismusorientierte Nutzer:innen ansprechen (clean, ruhig), aber auch Nutzer:innen ansprechen, die sich noch nicht mit weniger / besserem Konsum beschäftigt haben.
Es wäre toll folgende Slides zu haben:
- Anmeldung / Registrierung
- Quiz (Es soll direkt zu Beginn ein Quiz aus mehreren Slides geben, das Nutzer:innen einem Kauftypen zuordnet(
- Quizergebnis (Du bist Kauftyp XYZ...)
- Home-Screen der App / Navigation
- Statistiken: Du hast diesen Monat so viel gespart...
- Slide mit Einstellungen
- 'Challenge' Slide: 10 tage aussortieren

```html
<!DOCTYPE html>
<html lang="de">
<head>
<meta charset="utf-8">
<title>Bewusst – App Screens</title>
<link href="https://fonts.googleapis.com/css2?family=Manrope:wght@400;500;600;700;800&display=swap" rel="stylesheet">
<style>
:root{
  --green:#5f9e82;
  --green-dark:#4f8a70;
  --green-soft:#e6efe9;
  --ink:#23282b;
  --muted:#8b8f91;
  --line:#ecebe7;
  --bg:#f7f6f3;
  --card:#ffffff;
  --orange:#ef8a3c;
  --orange-soft:#fdf1e6;
  --red:#e25a5a;
}
*{box-sizing:border-box;margin:0;padding:0}
html,body{width:1027px;height:1200px;overflow:hidden;background:#fff;font-family:'Manrope',sans-serif;color:var(--ink)}
.stage{position:absolute;left:0;top:0;width:1785px;height:2087px;transform:scale(.5754);transform-origin:0 0}
.screen{position:absolute;width:376px;overflow:hidden;background:var(--bg);box-shadow:0 14px 30px rgba(0,0,0,.08)}
.abs{position:absolute}
.nav{position:absolute;left:0;right:0;bottom:0;height:74px;background:#fff;border-top:1px solid var(--line);display:flex;justify-content:space-around;padding:0 12px;align-items:center}
.nav-item{display:flex;flex-direction:column;align-items:center;gap:5px;font-size:8px;font-weight:700;letter-spacing:.5px;color:#6f7477;width:60px}
.nav-item svg{width:19px;height:19px;stroke:#6f7477;fill:none;stroke-width:1.7;stroke-linecap:round;stroke-linejoin:round}
.nav-item.active{color:var(--green)}
.nav-item.active svg{stroke:var(--green)}

/* welcome */
.welcome{left:67px;top:103px;height:776px;background:var(--green);color:#fff;text-align:center}
.welcome .art{left:53px;top:107px;width:260px;height:150px;border-radius:20px;background:linear-gradient(135deg,#7bb39a,#5a977c)}
.welcome h1{position:absolute;top:348px;left:20px;right:20px;font-size:25px;font-weight:700;line-height:31px}
.welcome p{position:absolute;top:422px;left:10px;right:10px;font-size:14.5px;line-height:24px;color:#e4f0ea}
.welcome .cta{left:30px;top:524px;width:315px;height:46px;border:1.5px solid #fff;border-radius:8px;display:flex;align-items:center;justify-content:center;gap:8px;font-size:13px;font-weight:700}

/* login */
.login{left:492px;top:103px;height:776px;background:#f3f2ef}
.login h1{position:absolute;top:68px;width:100%;text-align:center;font-size:24px;font-weight:600}
.tabs{left:46px;top:162px;width:290px;display:flex;font-size:16px;font-weight:600}
.tab{width:145px;text-align:center;padding-bottom:6px;color:#d4d3cf}
.tab.on{color:var(--green);border-bottom:3px solid var(--green)}
.label{font-size:13px;font-weight:600;position:absolute;left:30px}
.field{position:absolute;left:30px;width:316px;height:47px;border:1.5px solid #dedcd8;border-radius:8px;background:#f7f6f3;font-size:13px;padding:0 18px;display:flex;align-items:center;justify-content:space-between}
.field.error{border-color:var(--red);background:#fbf6f5;letter-spacing:1px;font-size:15px;font-weight:700}
.hint{position:absolute;top:411px;left:30px;right:30px;display:flex;justify-content:space-between;font-size:12px}
.btn-main{left:30px;top:443px;width:316px;height:47px;border-radius:7px;background:var(--green);color:#fff;font-size:13px;font-weight:700;display:flex;align-items:center;justify-content:center}
.divider{left:84px;top:519px;width:208px;display:flex;align-items:center;gap:14px;font-size:12px;color:#c8c6c2}
.divider i{flex:1;height:1px;background:#dedcd8}
.btn-alt{position:absolute;left:30px;width:316px;height:47px;border:1.5px solid #dedcd8;border-radius:8px;display:flex;align-items:center;justify-content:center;gap:8px;font-size:13px;font-weight:600}
.btn-alt b{width:14px;height:14px;border-radius:50%;background:var(--ink)}

/* quiz */
.quiz{left:917px;top:103px;height:776px;background:#fff}
.quiz .arrow{top:18px}
.quiz .step{left:20px;top:68px;font-size:12px;color:#6f7477}
.progress{left:20px;top:90px;width:335px;height:6px;background:#ecebe7;border-radius:3px}
.progress i{display:block;width:134px;height:100%;background:var(--green);border-radius:3px}
.quiz h2{position:absolute;top:164px;left:30px;right:30px;text-align:center;font-size:20px;font-weight:600;line-height:29px}
.option{position:absolute;left:27px;width:321px;height:57px;border:1px solid #eeedea;border-radius:8px;box-shadow:0 2px 6px rgba(0,0,0,.04);display:flex;align-items:center;justify-content:space-between;padding:0 18px;font-size:15px;font-weight:500}
.option i{width:16px;height:16px;border:1px solid #d8d7d3;border-radius:50%}

/* home */
.home{left:1342px;top:103px;height:776px}
.home .date{left:20px;top:30px;font-size:12px;color:#6f7477}
.home .hello{left:20px;top:50px;font-size:25px;font-weight:700}
.avatar{left:323px;top:50px;width:30px;height:30px;border-radius:50%;background:linear-gradient(135deg,#f2a55f,#d9553e)}
.insight{left:20px;top:101px;width:335px;height:233px;border-radius:24px;background:linear-gradient(135deg,var(--green),#78ad95);color:#fff;padding:22px 20px}
.insight small{font-size:11px;font-weight:600;letter-spacing:.6px;color:#e0eee7}
.insight h2{font-size:25px;font-weight:700;line-height:30px;margin-top:14px}
.insight p{font-size:14.5px;line-height:24px;margin-top:10px;color:#eaf4ef}
.pill{display:inline-block;margin-top:20px;background:rgba(255,255,255,.2);border-radius:14px;padding:6px 14px;font-size:12px;font-weight:600}
.section{position:absolute;left:20px;font-size:15px;font-weight:600}
.goal{left:20px;top:398px;width:335px;height:80px;border-radius:10px;background:#fff;overflow:hidden;display:flex;border-left:5px solid #f4b274}
.goal .txt{flex:1;padding:18px 18px}
.goal h3{font-size:15px;font-weight:700}
.goal p{font-size:11px;color:#6f7477;margin-top:6px}
.goal .pct{width:80px;background:var(--orange-soft);color:var(--orange);font-weight:700;font-size:20px;display:flex;align-items:center;justify-content:center}
.reflect{left:20px;top:542px;width:335px;height:148px;border-radius:16px;background:#f1f0ec;padding:20px}
.reflect p{font-size:16px;line-height:23px;width:240px}
.reflect .ring{position:absolute;right:16px;top:18px;width:60px;height:60px;border:3px solid #e4e3df;border-radius:50%}
.moods{display:flex;gap:12px;margin-top:18px}
.moods span{width:91px;height:45px;background:#fff;border-radius:8px;display:flex;align-items:center;justify-content:center}
.moods span i{width:18px;height:18px;border-radius:50%;background:#f5c542}

/* dinge */
.dinge{left:67px;top:927px;height:805px}
.dinge h1{position:absolute;left:20px;top:42px;font-size:21px;font-weight:700}
.plus{left:325px;top:40px;width:30px;height:30px;border-radius:50%;background:var(--green);color:#fff;font-size:18px;display:flex;align-items:center;justify-content:center}
.cats{left:20px;top:96px;width:335px;display:flex;justify-content:space-between}
.cat{width:72px;display:flex;flex-direction:column;align-items:center;gap:10px;font-size:8px;font-weight:600;color:#6f7477}
.cat .ic{width:48px;height:48px;border-radius:50%;display:flex;align-items:center;justify-content:center}
.cat .ic svg{width:20px;height:20px;fill:none;stroke-width:1.8;stroke-linecap:round;stroke-linejoin:round}
.cat.on{color:var(--ink)}
.item{position:absolute;left:21px;width:333px;height:73px;background:#fff;border-radius:10px;box-shadow:0 2px 8px rgba(0,0,0,.04);padding:18px 16px;display:flex;justify-content:space-between}
.item h3{font-size:15px;font-weight:600}
.item p{font-size:10px;color:#6f7477;margin-top:8px}
.item .price{text-align:right;font-size:14px;font-weight:600}
.item .price small{display:block;font-size:8px;font-weight:700;letter-spacing:.6px;color:var(--green);margin-top:10px}

/* trends */
.trends{left:495px;top:927px;height:1076px}
.trends h1{position:absolute;left:20px;top:42px;font-size:21px;font-weight:700}
.trends .sub{left:20px;top:75px;font-size:13px;color:#6f7477}
.focus{left:20px;top:121px;width:335px;height:113px;border-radius:18px;background:var(--green);color:#fff;padding:20px;overflow:hidden}
.focus small{font-size:10px;font-weight:700;letter-spacing:1px;color:#dcece4}
.focus h2{font-size:30px;font-weight:700;margin-top:4px}
.focus p{font-size:11px;color:#e6f1ec;margin-top:4px}
.focus .deco{position:absolute;right:-10px;top:0;width:90px;height:90px;border-radius:50%;border:8px solid rgba(255,255,255,.1)}
.stat{position:absolute;top:262px;width:161px;height:133px;background:#fff;border-radius:14px;text-align:center;padding-top:32px}
.stat small{font-size:11px;letter-spacing:1px;color:#6f7477}
.stat b{display:block;font-size:26px;font-weight:700;margin-top:6px}
.stat em{display:block;font-style:normal;font-size:9px;margin-top:6px}
.chart{left:20px;top:423px;width:335px;height:270px;background:#fff;border-radius:14px}
.chart h3{position:absolute;left:20px;top:22px;font-size:15px;font-weight:600}
.chart p{position:absolute;left:20px;top:50px;font-size:11px;color:#6f7477}
.days{position:absolute;left:22px;right:22px;top:222px;display:flex;justify-content:space-between;font-size:10px;color:#a4a7a9}
.ach{position:absolute;left:20px;width:335px;height:67px;background:#fff;border-radius:12px;display:flex;align-items:center;gap:14px;padding:0 14px}
.ach .ic{width:42px;height:42px;border-radius:8px;display:flex;align-items:center;justify-content:center}
.ach .ic svg{width:20px;height:20px;fill:none;stroke-width:1.7;stroke-linecap:round;stroke-linejoin:round}
.ach h4{font-size:12px;font-weight:700}
.ach p{font-size:9.5px;color:#6f7477;margin-top:2px}

/* challenge */
.challenge{left:917px;top:927px;height:1021px;background:#fff}
.ch-head{left:0;top:0;width:376px;height:187px;background:linear-gradient(135deg,#5f9e82,#76ac93);border-radius:0 0 26px 26px;color:#fff;padding:26px 26px}
.ch-head h1{font-size:25px;font-weight:700}
.ch-head p{font-size:15px;color:#e3f0e9;margin-top:10px}
.ch-prog{display:flex;align-items:center;gap:14px;margin-top:22px}
.ch-prog b{font-size:30px;font-weight:700}
.ch-prog i{flex:1;height:5px;background:rgba(255,255,255,.3);border-radius:3px;position:relative}
.ch-prog i::before{content:"";position:absolute;left:0;top:0;height:5px;width:48px;background:#fff;border-radius:3px}
.day{position:absolute;left:20px;width:336px;height:61px;background:#fff;border:1px solid #efeeeb;border-radius:8px;display:flex;align-items:center;gap:14px;padding:0 13px}
.day.done{background:var(--green-soft);border-color:#d9e6de}
.day .n{width:27px;height:27px;border-radius:50%;background:#efeeeb;font-size:9px;color:#6f7477;display:flex;align-items:center;justify-content:center}
.day.done .n{background:var(--green)}
.day h4{font-size:13px;font-weight:500}
.day.done h4{text-decoration:line-through;color:#8fa79b}
.day p{font-size:9.5px;color:#6f7477;margin-top:2px}

/* settings */
.settings{left:1342px;top:927px;height:700px}
.settings h1{position:absolute;left:20px;top:42px;font-size:21px;font-weight:700}
.cap{position:absolute;left:23px;font-size:11px;font-weight:700;letter-spacing:1px;color:#6f7477}
.group{position:absolute;left:20px;width:335px;background:#fff;border-radius:12px}
.row{height:66px;display:flex;align-items:center;gap:14px;padding:0 20px;border-bottom:1px solid var(--line)}
.row:last-child{border-bottom:none}
.row .ic{width:32px;height:32px;border-radius:50%;display:flex;align-items:center;justify-content:center}
.row .ic svg{width:15px;height:15px;fill:none;stroke-width:1.8;stroke-linecap:round;stroke-linejoin:round}
.row .t{flex:1}
.row h4{font-size:14px;font-weight:500}
.row p{font-size:9.5px;color:#6f7477;margin-top:2px}
.toggle{width:31px;height:17px;background:var(--green);border-radius:9px;position:relative}
.toggle::after{content:"";position:absolute;right:2px;top:2px;width:13px;height:13px;background:#fff;border-radius:50%}
.chip{font-size:9.5px;background:#efeeeb;color:#6f7477;padding:4px 12px;border-radius:10px}
.philo{left:20px;top:491px;width:335px;height:106px;border-radius:14px;background:#efeeea;border:1px solid #e4e3df;padding:20px 20px 0 20px;display:flex;gap:14px}
.philo h4{font-size:13px;font-weight:700}
.philo p{font-size:11px;font-style:italic;color:#6f7477;line-height:19px;margin-top:6px}
</style>
</head>
<body>
<div class="stage">

<!-- Welcome -->
<section class="screen welcome">
  <div class="abs art" role="img" aria-label="Illustration: entspannte Person liegt mit Tablet auf dem Rücken"></div>
  <h1>Entdecke, was dir wirklich guttut.</h1>
  <p>Lerne deine Konsumgewohnheiten<br>besser kennen – Schritt für Schritt, ohne Druck.</p>
  <div class="abs cta">Bist du bereit?
    <svg width="18" height="12" viewBox="0 0 18 12" fill="none" stroke="#fff" stroke-width="1.6" stroke-linecap="round" stroke-linejoin="round"><path d="M1 6h15M11 1l5 5-5 5"/></svg>
  </div>
</section>

<!-- Login -->
<section class="screen login">
  <h1>Lasst uns beginnen</h1>
  <div class="abs tabs"><span class="tab on">Anmelden</span><span class="tab">Registrieren</span></div>
  <span class="label" style="top:247px">E-Mail-Adresse</span>
  <div class="field" style="top:270px">hi@lenavoss.de</div>
  <span class="label" style="top:331px">Passwort</span>
  <div class="field error" style="top:354px">•••••••••••
    <svg width="18" height="14" viewBox="0 0 18 14" fill="none" stroke="#d8d6d2" stroke-width="1.4"><path d="M1 7s3-5 8-5 8 5 8 5-3 5-8 5-8-5-8-5z"/><circle cx="9" cy="7" r="2.5"/><path d="M2 13L16 1"/></svg>
  </div>
  <div class="hint"><span style="color:#dedcd8">Falsches Passwort</span><span style="color:var(--green);font-weight:600">Passwort vergessen?</span></div>
  <div class="abs btn-main">Weiter</div>
  <div class="abs divider"><i></i>Or<i></i></div>
  <div class="btn-alt" style="top:564px"><b></b>Mit Pomi anmelden</div>
  <div class="btn-alt" style="top:624px"><b style="background:var(--green)"></b>Mit Wendo anmelden</div>
</section>

<!-- Quiz -->
<section class="screen quiz">
  <svg class="abs arrow" style="left:22px" width="18" height="14" viewBox="0 0 18 14" fill="none" stroke="#555" stroke-width="1.6" stroke-linecap="round" stroke-linejoin="round"><path d="M17 7H2M7 1L1 7l6 6"/></svg>
  <svg class="abs arrow" style="right:22px" width="18" height="14" viewBox="0 0 18 14" fill="none" stroke="#555" stroke-width="1.6" stroke-linecap="round" stroke-linejoin="round"><path d="M1 7h15M11 1l6 6-6 6"/></svg>
  <span class="abs step">Frage 2 von 5</span>
  <div class="abs progress"><i></i></div>
  <h2>Welches Gefühl löst meistens deinen Kaufdrang aus?</h2>
  <div class="option" style="top:254px">Langeweile<i></i></div>
  <div class="option" style="top:326px">Stress<i></i></div>
  <div class="option" style="top:398px">Belohnung<i></i></div>
  <div class="option" style="top:470px">Inspiration<i></i></div>
</section>

<!-- Home -->
<section class="screen home">
  <span class="abs date">Mittwoch, 28. Jan</span>
  <span class="abs hello">Guten Morgen, Lena.</span>
  <div class="abs avatar" role="img" aria-label="Profilbild"></div>
  <div class="abs insight">
    <small>↗ WÖCHENTLICHER EINBLICK</small>
    <h2>3 bewusste Entscheidungen</h2>
    <p>Diese Woche hast du unnötige Ausgaben vermieden.</p>
    <span class="pill">42,00 € weniger ausgegeben</span>
  </div>
  <span class="section" style="top:362px">Aktives Ziel</span>
  <div class="abs goal"><div class="txt"><h3>7-Tage Konsum-Pause</h3><p>Tag 3 von 7 • Dranbleiben!</p></div><div class="pct">42%</div></div>
  <span class="section" style="top:506px">Tägliche Reflexion</span>
  <div class="abs reflect">
    <p>Wie hast du dich nach deinem letzten Kauf gefühlt?</p>
    <div class="ring"></div>
    <div class="moods"><span><i></i></span><span><i></i></span><span><i style="background:#e9b64a"></i></span></div>
  </div>
  <nav class="nav">
    <div class="nav-item active"><svg viewBox="0 0 24 24"><path d="M3 10l9-7 9 7v10a1 1 0 0 1-1 1h-5v-6h-6v6H4a1 1 0 0 1-1-1z"/></svg>HOME</div>
    <div class="nav-item"><svg viewBox="0 0 24 24"><path d="M12 2l9 5v10l-9 5-9-5V7z"/><path d="M3 7l9 5 9-5M12 12v10"/></svg>DINGE</div>
    <div class="nav-item"><svg viewBox="0 0 24 24"><path d="M2 17l7-7 4 4 8-8M15 6h6v6"/></svg>TRENDS</div>
    <div class="nav-item"><svg viewBox="0 0 24 24"><path d="M7 4h10v5a5 5 0 0 1-10 0zM7 6H4v2a3 3 0 0 0 3 3M17 6h3v2a3 3 0 0 1-3 3M12 14v4M8 21h8M9 18h6"/></svg>ZIELE</div>
    <div class="nav-item"><svg viewBox="0 0 24 24"><circle cx="12" cy="8" r="4"/><path d="M4 21a8 8 0 0 1 16 0"/></svg>PROFIL</div>
  </nav>
</section>

<!-- Dinge -->
<section class="screen dinge">
  <h1>Meine Dinge</h1>
  <div class="abs plus">+</div>
  <div class="abs cats">
    <div class="cat on"><div class="ic" style="background:#fde3ea"><svg viewBox="0 0 24 24" stroke="#e8457a"><path d="M12 20s-8-5-8-11a4.5 4.5 0 0 1 8-3 4.5 4.5 0 0 1 8 3c0 6-8 11-8 11z"/></svg></div>WUNSCH</div>
    <div class="cat"><div class="ic" style="background:#e3edfb"><svg viewBox="0 0 24 24" stroke="#5b8fd6"><rect x="4" y="6" width="16" height="14" rx="2"/><path d="M9 10a3 3 0 0 0 6 0M8 6V4h8v2"/></svg></div>GEKAUFT</div>
    <div class="cat"><div class="ic" style="background:#e8efeb"><svg viewBox="0 0 24 24" stroke="#9bb5a8"><circle cx="12" cy="12" r="8"/><path d="M9 9l6 6M15 9l-6 6"/></svg></div>VERZICHTET</div>
    <div class="cat"><div class="ic" style="background:#fdeee0"><svg viewBox="0 0 24 24" stroke="#ef9a52"><path d="M4 7h16M9 7V4h6v3M6 7l1 13h10l1-13M10 11v6M14 11v6"/></svg></div>AUSGEMISTET</div>
  </div>
  <div class="item" style="top:190px"><div><h3>Espressomaschine</h3><p>Seit 1 Woche</p></div><div class="price">450,00 €<small>REFLEKTIEREN</small></div></div>
  <div class="item" style="top:285px"><div><h3>Noise-Cancelling Kopfhörer</h3><p>Vor 2 Tagen</p></div><div class="price">289,00 €<small>REFLEKTIEREN</small></div></div>
  <div class="item" style="top:380px"><div><h3>Neuer Bürostuhl</h3><p>Seit 5 Tagen</p></div><div class="price">349,00 €<small>REFLEKTIEREN</small></div></div>
  <div class="item" style="top:475px"><div><h3>Wochenend-Kurztrip</h3><p>Vor 2 Tagen</p></div><div class="price">400,00 €<small>REFLEKTIEREN</small></div></div>
  <div class="item" style="top:570px"><div><h3>Smartwatch</h3><p>Vor 2 Tagen</p></div><div class="price">199,00 €<small>REFLEKTIEREN</small></div></div>
  <div class="item" style="top:665px"><div><h3>Minimalistische Stehlampe</h3><p>Vor 2 Tagen</p></div><div class="price">159,00 €<small>REFLEKTIEREN</small></div></div>
  <nav class="nav">
    <div class="nav-item"><svg viewBox="0 0 24 24"><path d="M3 10l9-7 9 7v10a1 1 0 0 1-1 1h-5v-6h-6v6H4a1 1 0 0 1-1-1z"/></svg>HOME</div>
    <div class="nav-item active"><svg viewBox="0 0 24 24"><path d="M12 2l9 5v10l-9 5-9-5V7z"/><path d="M3 7l9 5 9-5M12 12v10"/></svg>DINGE</div>
    <div class="nav-item"><svg viewBox="0 0 24 24"><path d="M2 17l7-7 4 4 8-8M15 6h6v6"/></svg>TRENDS</div>
    <div class="nav-item"><svg viewBox="0 0 24 24"><path d="M7 4h10v5a5 5 0 0 1-10 0zM7 6H4v2a3 3 0 0 0 3 3M17 6h3v2a3 3 0 0 1-3 3M12 14v4M8 21h8M9 18h6"/></svg>ZIELE</div>
    <div class="nav-item"><svg viewBox="0 0 24 24"><circle cx="12" cy="8" r="4"/><path d="M4 21a8 8 0 0 1 16 0"/></svg>PROFIL</div>
  </nav>
</section>

<!-- Trends -->
<section class="screen trends">
  <h1>Bewusstseins-Trends</h1>
  <span class="abs sub">Deine psychologische Entwicklung.</span>
  <div class="abs focus">
    <div class="deco"></div>
    <small>⚡ FOKUS SCORE</small>
    <h2>+85%</h2>
    <p>Deine Impulskontrolle steigt stetig an.</p>
  </div>
  <div class="stat" style="left:20px"><small>GESPART</small><b style="color:var(--green)">420€</b><em style="color:var(--green)">Diesen Monat</em></div>
  <div class="stat" style="left:195px"><small>MINDFUL</small><b style="color:var(--orange)">12</b><em style="color:var(--orange)">Kaufmomente</em></div>
  <div class="abs chart">
    <h3>Psychologie &amp; Fokus</h3>
    <p>Mentale Stärke im Zeitverlauf</p>
    <svg class="abs" style="left:0;top:0" width="335" height="270" viewBox="0 0 335 270">
      <defs><linearGradient id="area" x1="0" y1="0" x2="0" y2="1"><stop offset="0" stop-color="#5f9e82" stop-opacity=".3"/><stop offset="1" stop-color="#5f9e82" stop-opacity="0"/></linearGradient></defs>
      <path d="M25 195 C60 180 100 155 125 152 C150 149 165 165 180 160 C195 155 205 140 230 128 C260 115 285 108 312 105 L312 215 L25 215 Z" fill="url(#area)"/>
      <path d="M25 195 C60 180 100 155 125 152 C150 149 165 165 180 160 C195 155 205 140 230 128 C260 115 285 108 312 105" fill="none" stroke="#5f9e82" stroke-width="3" stroke-linecap="round"/>
    </svg>
    <div class="days"><span>Di</span><span>Mi</span><span>Do</span><span>Fr</span><span>Sa</span><span>So</span></div>
  </div>
  <span class="section" style="top:724px">Erfolge</span>
  <div class="ach" style="top:761px"><div class="ic" style="background:#e6eefb"><svg viewBox="0 0 24 24" stroke="#5b8fd6"><circle cx="12" cy="12" r="8"/><path d="M12 4v16M8 8c2 1 2 3 0 4M16 8c-2 1-2 3 0 4"/></svg></div><div><h4>Ruhepol</h4><p>3 Tage ohne Impulskauf</p></div></div>
  <div class="ach" style="top:840px"><div class="ic" style="background:#fdf6dc"><svg viewBox="0 0 24 24" stroke="#e9b32e"><path d="M12 3l2.7 5.6 6.1.9-4.4 4.3 1 6.1L12 17l-5.4 2.9 1-6.1L3.2 9.5l6.1-.9z"/></svg></div><div><h4>Meister</h4><p>10 Dinge ausgemistet</p></div></div>
  <div class="ach" style="top:919px"><div class="ic" style="background:#e6efe9"><svg viewBox="0 0 24 24" stroke="#5f9e82"><path d="M12 3l8 3v6c0 5-4 8-8 9-4-1-8-4-8-9V6z"/><path d="M9 12l2 2 4-4"/></svg></div><div><h4>Bewusst</h4><p>Quiz abgeschlossen</p></div></div>
  <nav class="nav">
    <div class="nav-item"><svg viewBox="0 0 24 24"><path d="M3 10l9-7 9 7v10a1 1 0 0 1-1 1h-5v-6h-6v6H4a1 1 0 0 1-1-1z"/></svg>HOME</div>
    <div class="nav-item"><svg viewBox="0 0 24 24"><path d="M12 2l9 5v10l-9 5-9-5V7z"/><path d="M3 7l9 5 9-5M12 12v10"/></svg>DINGE</div>
    <div class="nav-item active"><svg viewBox="0 0 24 24"><path d="M2 17l7-7 4 4 8-8M15 6h6v6"/></svg>TRENDS</div>
    <div class="nav-item"><svg viewBox="0 0 24 24"><path d="M7 4h10v5a5 5 0 0 1-10 0zM7 6H4v2a3 3 0 0 0 3 3M17 6h3v2a3 3 0 0 1-3 3M12 14v4M8 21h8M9 18h6"/></svg>ZIELE</div>
    <div class="nav-item"><svg viewBox="0 0 24 24"><circle cx="12" cy="8" r="4"/><path d="M4 21a8 8 0 0 1 16 0"/></svg>PROFIL</div>
  </nav>
</section>

<!-- Challenge -->
<section class="screen challenge">
  <div class="abs ch-head">
    <h1>10 Tage Ausmisten</h1>
    <p>Platz schafft Klarheit.</p>
    <div class="ch-prog"><b>20%</b><i></i></div>
  </div>
  <div class="day done" style="top:208px"><span class="n"><svg width="12" height="10" viewBox="0 0 12 10" fill="none" stroke="#fff" stroke-width="2" stroke-linecap="round" stroke-linejoin="round"><path d="M1 5l3.5 3.5L11 1.5"/></svg></span><div><h4>Tag 1</h4><p>Schreibtisch aufräumen</p></div></div>
  <div class="day done" style="top:283px"><span class="n"><svg width="12" height="10" viewBox="0 0 12 10" fill="none" stroke="#fff" stroke-width="2" stroke-linecap="round" stroke-linejoin="round"><path d="M1 5l3.5 3.5L11 1.5"/></svg></span><div><h4>Tag 2</h4><p>Kleiderschrank checken</p></div></div>
  <div class="day" style="top:359px"><span class="n">3</span><div><h4>Tag 3</h4><p>Eine Sache spenden</p></div></div>
  <div class="day" style="top:434px"><span class="n">4</span><div><h4>Tag 4</h4><p>Eine Sache spenden</p></div></div>
  <div class="day" style="top:510px"><span class="n">5</span><div><h4>Tag 5</h4><p>Eine Sache spenden</p></div></div>
  <div class="day" style="top:585px"><span class="n">6</span><div><h4>Tag 6</h4><p>Eine Sache spenden</p></div></div>
  <div class="day" style="top:661px"><span class="n">7</span><div><h4>Tag 7</h4><p>Eine Sache spenden</p></div></div>
  <div class="day" style="top:736px"><span class="n">8</span><div><h4>Tag 8</h4><p>Eine Sache spenden</p></div></div>
  <div class="day" style="top:812px"><span class="n">9</span><div><h4>Tag 9</h4><p>Eine Sache spenden</p></div></div>
  <div class="day" style="top:887px"><span class="n">10</span><div><h4>Tag 10</h4><p>Eine Sache spenden</p></div></div>
  <nav class="nav">
    <div class="nav-item"><svg viewBox="0 0 24 24"><path d="M3 10l9-7 9 7v10a1 1 0 0 1-1 1h-5v-6h-6v6H4a1 1 0 0 1-1-1z"/></svg>HOME</div>
    <div class="nav-item"><svg viewBox="0 0 24 24"><path d="M12 2l9 5v10l-9 5-9-5V7z"/><path d="M3 7l9 5 9-5M12 12v10"/></svg>DINGE</div>
    <div class="nav-item"><svg viewBox="0 0 24 24"><path d="M2 17l7-7 4 4 8-8M15 6h6v6"/></svg>TRENDS</div>
    <div class="nav-item active"><svg viewBox="0 0 24 24"><path d="M7 4h10v5a5 5 0 0 1-10 0zM7 6H4v2a3 3 0 0 0 3 3M17 6h3v2a3 3 0 0 1-3 3M12 14v4M8 21h8M9 18h6"/></svg>ZIELE</div>
    <div class="nav-item"><svg viewBox="0 0 24 24"><circle cx="12" cy="8" r="4"/><path d="M4 21a8 8 0 0 1 16 0"/></svg>PROFIL</div>
  </nav>
</section>

<!-- Settings -->
<section class="screen settings">
  <h1>Einstellungen</h1>
  <span class="cap" style="top:96px">PRÄFERENZEN</span>
  <div class="group" style="top:131px">
    <div class="row"><span class="ic" style="background:#efeeeb"><svg viewBox="0 0 24 24" stroke="#8b8f91"><path d="M6 16V11a6 6 0 0 1 12 0v5l2 2H4zM10 21h4"/></svg></span><div class="t"><h4>Sanfte Erinnerungen</h4><p>Morgens &amp; Abends</p></div><span class="toggle"></span></div>
    <div class="row"><span class="ic" style="background:#fdeee0"><svg viewBox="0 0 24 24" stroke="#ef8a3c"><path d="M20 14A8 8 0 1 1 10 4a6 6 0 0 0 10 10z"/></svg></span><div class="t"><h4>Erscheinungsbild</h4><p>Hell (Standard)</p></div><span class="chip">Light</span></div>
  </div>
  <span class="cap" style="top:295px">MINDFUL TOOLKIT</span>
  <div class="group" style="top:330px">
    <div class="row"><span class="ic" style="background:#e6eefb"><svg viewBox="0 0 24 24" stroke="#5b8fd6"><path d="M12 3l8 3v6c0 5-4 8-8 9-4-1-8-4-8-9V6z"/></svg></span><div class="t"><h4>Impuls-Pause</h4></div><svg width="8" height="12" viewBox="0 0 8 12" fill="none" stroke="#555" stroke-width="1.6"><path d="M1 1l5 5-5 5"/></svg></div>
    <div class="row"><span class="ic" style="background:#fde3ea"><svg viewBox="0 0 24 24" stroke="#e8457a"><path d="M12 20s-8-5-8-11a4.5 4.5 0 0 1 8-3 4.5 4.5 0 0 1 8 3c0 6-8 11-8 11z"/></svg></span><div class="t"><h4>Freuden-Check</h4></div><svg width="8" height="12" viewBox="0 0 8 12" fill="none" stroke="#555" stroke-width="1.6"><path d="M1 1l5 5-5 5"/></svg></div>
  </div>
  <div class="abs philo">
    <svg width="20" height="20" viewBox="0 0 24 24" fill="none" stroke="#5f9e82" stroke-width="1.8" stroke-linecap="round"><circle cx="12" cy="12" r="9"/><path d="M12 11v6M12 7.5v.5"/></svg>
    <div><h4>Unsere Philosophie</h4><p>“Bewusster Konsum bedeutet keinen Verzicht – sondern Klarheit darüber, was wirklich zählt.”</p></div>
  </div>
  <nav class="nav">
    <div class="nav-item"><svg viewBox="0 0 24 24"><path d="M3 10l9-7 9 7v10a1 1 0 0 1-1 1h-5v-6h-6v6H4a1 1 0 0 1-1-1z"/></svg>HOME</div>
    <div class="nav-item"><svg viewBox="0 0 24 24"><path d="M12 2l9 5v10l-9 5-9-5V7z"/><path d="M3 7l9 5 9-5M12 12v10"/></svg>DINGE</div>
    <div class="nav-item"><svg viewBox="0 0 24 24"><path d="M2 17l7-7 4 4 8-8M15 6h6v6"/></svg>TRENDS</div>
    <div class="nav-item"><svg viewBox="0 0 24 24"><path d="M7 4h10v5a5 5 0 0 1-10 0zM7 6H4v2a3 3 0 0 0 3 3M17 6h3v2a3 3 0 0 1-3 3M12 14v4M8 21h8M9 18h6"/></svg>ZIELE</div>
    <div class="nav-item active"><svg viewBox="0 0 24 24"><circle cx="12" cy="8" r="4"/><path d="M4 21a8 8 0 0 1 16 0"/></svg>PROFIL</div>
  </nav>
</section>

</div>
</body>
</html>
```